Dune crest Website

We need a simple web page design for our businessWe procure and dispose of earthmoving construction equipmentwe also find construction equipment for our customers using our global contacts

Number of Pages Required

1 page

```html
<!DOCTYPE html>
<html lang="en">
<head>
<meta charset="utf-8">
<title>Dune Crest — Earthmoving</title>
<link rel="stylesheet" href="https://fonts.googleapis.com/css2?family=Raleway:wght@400;500;600;700;800&display=swap">
<style>
  :root {
    --red: #e0301e;
    --ink: #2f2f2f;
    --text: #6b6b6b;
    --white: #ffffff;
    --panel: #f0f0f0;
    --panel-light: #f8f8f8;
    --footer: #2d2d2d;
    --footer-text: #9a9a9a;
  }
  * { box-sizing: border-box; margin: 0; padding: 0; }
  html, body { width: 689px; height: 1200px; overflow: hidden; background: var(--white); }
  body { position: relative; font-family: "Raleway", Arial, sans-serif; color: var(--text); }
  .abs { position: absolute; }

  /* Header */
  .site-header { left: 0; top: 0; width: 689px; height: 45px; background: var(--white); }
  .brand { left: 78px; top: 14px; display: flex; align-items: center; gap: 5px; }
  .brand-mark { width: 9px; height: 9px; background: var(--red); }
  .brand-name { font-weight: 800; font-size: 14px; letter-spacing: 0.5px; color: var(--ink); }
  .main-nav a { position: absolute; top: 22px; font-size: 5.6px; font-weight: 700; color: var(--ink); text-decoration: none; letter-spacing: 0.2px; }
  .call-button { left: 537px; top: 14px; width: 76px; height: 21px; background: var(--red); border-radius: 2px; color: var(--white); font-size: 7px; font-weight: 700; display: flex; align-items: center; justify-content: center; gap: 4px; }

  /* Hero */
  .hero { left: 0; top: 45px; width: 689px; height: 294px; background: linear-gradient(160deg, #55575a 0%, #3d3f41 40%, #5c574a 65%, #4a4844 100%); }
  .hero-title { left: 0; top: 124px; width: 689px; text-align: center; font-size: 31px; font-weight: 800; color: var(--white); letter-spacing: 0.5px; }
  .hero-text { left: 184px; top: 171px; width: 340px; text-align: center; font-size: 6.3px; line-height: 14px; color: var(--white); }
  .hero-button { left: 284px; top: 213px; width: 113px; height: 29px; background: var(--red); border-radius: 2px; color: var(--white); font-size: 7.5px; font-weight: 800; display: flex; align-items: center; justify-content: center; }
  .hero-arrow { top: 169px; }

  /* Welcome */
  .welcome-title { left: 0; top: 364px; width: 689px; text-align: center; font-size: 12.5px; font-weight: 800; color: var(--ink); }
  .welcome-text { left: 122px; width: 444px; text-align: center; font-size: 6.2px; line-height: 13.8px; }

  /* Feature rows */
  .photo { background: #888; }
  .row-panel { height: 199px; }
  .row-title { font-size: 10.6px; font-weight: 800; color: var(--ink); line-height: 16px; }
  .row-text { font-size: 6.2px; line-height: 13.8px; }
  .read-more { width: 70px; height: 21px; background: var(--red); border-radius: 2px; color: var(--white); font-size: 6px; font-weight: 800; display: flex; align-items: center; justify-content: center; }

  /* Featured work */
  .featured-title { left: 0; top: 928px; width: 689px; text-align: center; font-size: 12.5px; font-weight: 800; color: var(--ink); }
  .work-tile { top: 963px; width: 170px; height: 106px; }

  /* Contact band */
  .contact-band { left: 0; top: 1099px; width: 689px; height: 70px; background: var(--red); }
  .contact-item { top: 1121px; display: flex; gap: 10px; color: var(--white); }
  .contact-item strong { display: block; font-size: 7.8px; font-weight: 700; margin-bottom: 3px; }
  .contact-item span { display: block; font-size: 5.8px; line-height: 10px; }

  /* Footer */
  .site-footer { left: 0; top: 1169px; width: 689px; height: 31px; background: var(--footer); }
  .copyright { left: 77px; top: 1183px; font-size: 5px; color: var(--footer-text); }
  .social-square { top: 1180px; width: 10px; height: 10px; background: var(--red); border-radius: 1px; }
</style>
</head>
<body>

<header class="site-header abs">
  <div class="brand abs"><span class="brand-mark"></span><span class="brand-name">DUNE CREST</span></div>
  <nav class="main-nav">
    <a class="abs" style="left:277px">HOME</a>
    <a class="abs" style="left:319px">ABOUT US</a>
    <a class="abs" style="left:375px">SERVICES</a>
    <a class="abs" style="left:427px">EQUIPMENT</a>
    <a class="abs" style="left:487px">CONTACT US</a>
  </nav>
  <div class="call-button abs">
    <svg width="7" height="7" viewBox="0 0 24 24"><path fill="#fff" d="M6.6 10.8a15.1 15.1 0 0 0 6.6 6.6l2.2-2.2c.3-.3.7-.4 1-.2 1.1.4 2.3.6 3.6.6.6 0 1 .4 1 1V20c0 .6-.4 1-1 1A17 17 0 0 1 3 4c0-.6.4-1 1-1h3.5c.6 0 1 .4 1 1 0 1.3.2 2.5.6 3.6.1.3 0 .7-.2 1z"/></svg>
    0400 218 764
  </div>
</header>

<section class="hero abs" role="img" aria-label="Yellow excavator digging on a rocky mountain site under a grey sky"></section>
<h1 class="hero-title abs">EARTHMOVING</h1>
<p class="hero-text abs">Mauris volutpat nulla a enim efficitur elementum poritor at diam aliquam et elit elementum, fermentum nisl sed, pellentesque mares. Integer blandit erat bibendum pulvinar lobortis. Mauris sed turpis.</p>
<div class="hero-button abs">OUR SERVICES</div>
<svg class="hero-arrow abs" style="left:56px" width="8" height="12" viewBox="0 0 8 12"><path d="M6 1 1.5 6 6 11" fill="none" stroke="#fff" stroke-width="1.5"/></svg>
<svg class="hero-arrow abs" style="left:621px" width="8" height="12" viewBox="0 0 8 12"><path d="M2 1 6.5 6 2 11" fill="none" stroke="#fff" stroke-width="1.5"/></svg>

<h2 class="welcome-title abs">WELCOME TO DUNE CREST SERVICE</h2>
<p class="welcome-text abs" style="top:390px">Mauris volutpat nulla a enim efficitur elementum poritor at diam aliquam et elit elementum, fermentum nisl sed, pellentesque mares. Integer blandit erat bibendum pulvinar lobortis. Mauris sed turpis.</p>
<p class="welcome-text abs" style="top:431px">Nulla vitae dui et velit sagittis fermentum. Donec rhocus tincidun. Nullam nibh tellus, blandit vel leo vulputate, commodo edmentum. Pellentesque eget quam ultrices, semperos lacus et, lacinia neue. Class aptent taciti sociosqu ad litora torquent per conubia nostra, per inceptos himenaeos. In id accumsan augue. Mauris ultricores, metus quis tempor sagittis, tellus lectus pharetra massa, ut ultces.</p>

<div class="photo abs" style="left:0;top:504px;width:342px;height:199px;background:radial-gradient(circle at 62% 38%, #ffe08a 0%, #f0a020 18%, #b8680c 45%, #3a2206 80%, #120a02 100%)" role="img" aria-label="Bulldozer silhouette against an orange sunset"></div>
<div class="row-panel abs" style="left:342px;top:504px;width:347px;background:var(--panel)"></div>
<h3 class="row-title abs" style="left:371px;top:532px">EARTHMOVING<br>CONSTRUCTION EQUIPMENT</h3>
<p class="row-text abs" style="left:371px;top:569px;width:210px">Dune crest provides complete site work services for commercial, industrial, subdivision and road projects throughout the state of Florida - and beyond. We specialize in professional, time-efficient project turnaround. We get in, get out, and do it right the first time!</p>
<div class="read-more abs" style="left:374px;top:647px">READ MORE</div>

<div class="row-panel abs" style="left:0;top:703px;width:342px;background:var(--panel-light)"></div>
<h3 class="row-title abs" style="left:100px;top:739px;width:213px;text-align:right">CONSTRUCTION EQUIPMENT</h3>
<p class="row-text abs" style="left:103px;top:763px;width:210px;text-align:right">construction equipment for our customers using our global contacts. Dune crest provides complete site work services for commercial, industrial, subdivision and road projects throughout the state of Florida - and beyond. We specialize in professional, time-efficient project turnaround. We get in, get out, and do it right the first time!</p>
<div class="read-more abs" style="left:244px;top:857px">READ MORE</div>
<div class="photo abs" style="left:342px;top:703px;width:347px;height:199px;background:linear-gradient(135deg, #9aa3a6 0%, #7d8588 45%, #b45a3a 70%, #6f777a 100%)" role="img" aria-label="Workers in orange vests tying rebar on a construction deck"></div>

<h2 class="featured-title abs">FEATURED WORK</h2>
<div class="work-tile photo abs" style="left:77px;background:linear-gradient(180deg, #7fa6c8 0%, #b9a88a 55%, #d27a3a 100%)" role="img" aria-label="Orange excavator at a city building site"></div>
<div class="work-tile photo abs" style="left:261px;background:linear-gradient(180deg, #c5d6e4 0%, #8e9aa4 55%, #6c7278 100%)" role="img" aria-label="Engineer reviewing plans above a city skyline"></div>
<div class="work-tile photo abs" style="left:442px;background:linear-gradient(180deg, #5d7fa8 0%, #a8764a 50%, #b4451e 100%)" role="img" aria-label="Dump truck and excavator on red earth"></div>

<footer>
  <div class="contact-band abs"></div>
  <div class="contact-item abs" style="left:88px">
    <svg width="16" height="14" viewBox="0 0 24 20"><path fill="#fff" d="M12 1 1 10h3v9h6v-6h4v6h6v-9h3z"/></svg>
    <div><strong>Leon Hartley</strong><span>Harbor Building</span><span>Portland, OR 97204</span></div>
  </div>
  <div class="contact-item abs" style="left:272px">
    <svg width="16" height="12" viewBox="0 0 24 18"><rect x="1" y="1" width="22" height="16" rx="2" fill="#fff"/><path d="M2 3l10 7 10-7" fill="none" stroke="#e0301e" stroke-width="2"/></svg>
    <div><strong>leon@dunecrestworks.com</strong><span>Drop us a line anytime!</span></div>
  </div>
  <div class="contact-item abs" style="left:474px">
    <svg width="14" height="14" viewBox="0 0 24 24"><path fill="#fff" d="M6.6 10.8a15.1 15.1 0 0 0 6.6 6.6l2.2-2.2c.3-.3.7-.4 1-.2 1.1.4 2.3.6 3.6.6.6 0 1 .4 1 1V20c0 .6-.4 1-1 1A17 17 0 0 1 3 4c0-.6.4-1 1-1h3.5c.6 0 1 .4 1 1 0 1.3.2 2.5.6 3.6.1.3 0 .7-.2 1z"/></svg>
    <div><strong>0 (855) 410-2967</strong><span>Call us now.</span></div>
  </div>
  <div class="site-footer abs"></div>
  <p class="copyright abs">© 2018 dunecrestworks.com. All rights reserved.</p>
  <span class="social-square abs" style="left:555px"></span>
  <span class="social-square abs" style="left:570px"></span>
  <span class="social-square abs" style="left:585px"></span>
  <span class="social-square abs" style="left:600px"></span>
</footer>

</body>
</html>
```